Rice Cakes Packing Desing

We need a simple (4 color) yet colorful, atractive design for a Rice Cake polypropylene bag. We are expanding our line to include 8-10 different flavors with each bag being a different color for easy identificaction. We are starting right with the first design. We already have "sample model" (of an existing product in the usa market) upon which we believe that our design could be based on (as an idea of a simple 4 color plastic bag design), which we are including in this post. We are also including an image of Brindle Rice Cakes plastic bag that has a round front window that shows the product inside the bag, which we also would like to include in our design. We already have a brand name and a logo design. The bag's dimension is about 20cms (wide) 30cms (tall) and it will contain about 12 rice cakes inside. (I HAVE ATTACHED A COUPLE OF IMAGES OF A PRINTED POLYPROPYLENE RICE CAKES BAG FOR YOUR REFERENCE)
Updates

Project Deadline Extended
Reason: We want to provide the designers with NUTRITIONAL INFORMATION, Bar Code, Company information, Ingredients, important pointers, etc. to be incorporated into the design. We would like to provide a few more days in order to fully integrate the back & front text into the package design in order to attain a perfectly balanced and well presented package. So far we have received some very interesting and highly viable proposals and we would like to provide the designers the necessary text information in order to have a complete, fully designed, great-looking package. We feel that with the extension the final design can be completed and we can have an opportunity to review, incorporate/change/modify any details before choosing the final design. Great designs have been submitted and we will definitely choose one before the newly proposed deadline. Thanks to all!

Target Market(s)

Although the concept of RICE CAKES might very well have its origins in ASIA the idea is to create a design (logo & pack) that will convey a message to the end consumer that our brand name stands for "FRESHNESS", "HEALTHY", "(removed with logo)", "TOP GRAINS", "GOODNESS", in short if you consume are products "IT IS GOOD FOR YOU!" (not only for people who love oriental food). We would like to have a product image that says "Hey! This looks Healthy & Tasty" (non-fattening, yummy and good!)

When you buy a pack of GRANOLAS what do you think about? What do you believe it is that you are buying? Good, Healthy Stuff? Good Tasting? Good for you? That's the idea!

Besides Rice Cakes are super light, fluffy, crunchy and easy to digest that it makes it a great Snack for everyone! Kids & Adults!

We need the full complete design of the actual bag (where the Rice Cakes will be packed) in order to start production of the bags right.

Industry/Entity Type

Plastic

Requirements
Must have
• We already have a local company in Mexico City that makes printed polypropylene bags. They are only waiting for the bag design in order to print the 20cms x 30cms bags.
Kindly consider that on the back Nutritional Information will be needed as well as a BarCode, company information, some bullets (pointing to the most important benefits of the product), etc. We will provide all the text information.
Nice to have
• Kindly take a look at the newly uploaded images from "VORNEP" Rice Cake packages. They are a good example of how to accomplish a great looking design using only 4 colors (which saves a lot in printing costs)
Should not have
• We do NOT want to have a design that says "This is ORIENTAL food". We don't want it to appear like "Sushi Rice" or "Japanese food", etc.

```html
<!DOCTYPE html>
<html lang="en">
<head>
<meta charset="utf-8">
<title>Halden Foods Rice Cakes – Bag Front</title>
<link rel="stylesheet" href="https://fonts.googleapis.com/css2?family=Open+Sans:wght@300;400;600&family=PT+Sans+Narrow:wght@700&family=Parisienne&display=swap">
<style>
  :root {
    --gold: #a19265;
    --sky: #7fcff0;
    --sky-light: #9adaf4;
    --orange: #f3ad35;
    --charcoal: #58585a;
    --white: #ffffff;
    --crumb: #d9d0bd;
  }
  * { box-sizing: border-box; margin: 0; padding: 0; }
  html, body { width: 887px; height: 1200px; overflow: hidden; background: var(--white); }
  .canvas { position: relative; width: 887px; height: 1200px; font-family: "Open Sans", sans-serif; }

  .swatch { position: absolute; left: 11px; width: 36px; height: 36px; }
  .swatch--gold { top: 11px; background: var(--gold); }
  .swatch--sky { top: 58px; background: var(--sky); }
  .swatch--orange { top: 114px; background: var(--orange); }
  .swatch--charcoal { top: 163px; background: var(--charcoal); }

  .bag-front { position: absolute; left: 94px; top: 49px; width: 787px; height: 1140px; overflow: hidden; background: var(--sky); }
  .bag-pattern { position: absolute; inset: 0; background: linear-gradient(160deg, var(--sky-light) 0%, var(--sky) 28%, var(--sky) 100%); }

  .band { position: absolute; left: 0; width: 100%; background: var(--orange); color: var(--white); }
  .band--top { top: 278px; height: 42px; }
  .band--bottom { top: 960px; height: 39px; }
  .band-label { position: absolute; top: 50%; transform: translateY(-50%); font-weight: 400; font-size: 22px; letter-spacing: 1.5px; }
  .band-label--left { left: 83px; }
  .band-label--right { left: 557px; }

  .brand-badge { position: absolute; left: 233px; top: 228px; width: 328px; height: 328px; border-radius: 50%; background: var(--white); display: flex; align-items: center; justify-content: center; }
  .brand-name { font-weight: 600; font-size: 40px; color: var(--gold); letter-spacing: 1px; }

  .flavour { position: absolute; left: 0; width: 794px; top: 554px; text-align: center; color: var(--white); font-size: 27px; font-weight: 600; letter-spacing: 3px; }

  .product-name { position: absolute; left: 50px; top: 620px; font-family: "Parisienne", cursive; line-height: 1; }
  .product-name__rice { display: block; font-size: 96px; color: var(--charcoal); margin-left: 14px; }
  .product-name__cakes { display: block; font-size: 150px; color: var(--white); -webkit-text-stroke: 2px var(--orange); margin-top: -40px; }

  .benefits { position: absolute; left: 502px; top: 622px; list-style: none; font-family: "PT Sans Narrow", sans-serif; font-weight: 700; font-size: 25px; color: var(--gold); }
  .benefits li { height: 44px; }
  .benefits li::before { content: "•"; margin-right: 10px; }

  .free-from { position: absolute; left: 14px; top: 925px; color: var(--white); font-size: 16px; letter-spacing: -0.3px; }

  .window { position: absolute; left: 425px; top: 746px; width: 328px; height: 328px; border-radius: 50%; background: var(--white); }
  .window__product { position: absolute; left: 14px; top: 14px; width: 300px; height: 300px; border-radius: 50%; background: radial-gradient(circle at 45% 40%, #ece6d8 0%, var(--crumb) 60%, #b9ab90 100%); }

  .net-weight { position: absolute; left: 13px; top: 1060px; font-weight: 300; font-size: 34px; color: var(--charcoal); }
</style>
</head>
<body>
<div class="canvas">
  <div class="swatch swatch--gold"></div>
  <div class="swatch swatch--sky"></div>
  <div class="swatch swatch--orange"></div>
  <div class="swatch swatch--charcoal"></div>

  <section class="bag-front">
    <div class="bag-pattern" role="img" aria-label="Faint pattern of wheat stalks on sky blue"></div>

    <div class="band band--top">
      <span class="band-label band-label--left">FRESHNESS</span>
      <span class="band-label band-label--right">12 RICE CAKES</span>
    </div>

    <div class="brand-badge"><span class="brand-name">HALDEN FOODS</span></div>

    <p class="flavour">LIGHTLY SALTED</p>

    <h1 class="product-name">
      <span class="product-name__rice">rice</span>
      <span class="product-name__cakes">cakes</span>
    </h1>

    <ul class="benefits">
      <li>30 CALORIES PER SLICE</li>
      <li>NATURAL INGREDIENTS</li>
      <li>WHOLE GRAIN</li>
    </ul>

    <p class="free-from">NO TRANS FAT - NO PRESERVATIVES - NO FOOD COLORS</p>

    <div class="band band--bottom">
      <span class="band-label band-label--left">GLUTEN FREE</span>
    </div>

    <div class="window">
      <div class="window__product" role="img" aria-label="Window showing a stack of rice cakes"></div>
    </div>

    <p class="net-weight">NET WT 3.5 OZ {100gr}</p>
  </section>
</div>
</body>
</html>
```